Wren Sporting Goods Inc.

Need to create a website that is informational and has the ability to sell goods and services. Such as a custom t shirt designer where the user can upload and image to be displayed on the garmet. The sports we specialize in are basketball, football, and baseball.

Would like like:
Home Page
Locker Room Page:
Custom Uniforms Page
Custom Shirt Creator
Brands
About

Competitor websites are
tundrafieldwearnx.com
dvq.com
lumarogear.com

```html
<!DOCTYPE html>
<html lang="en">
<head>
<meta charset="utf-8">
<title>Wren Sporting Goods — Custom Team Apparel</title>
<link href="https://fonts.googleapis.com/css2?family=Lexend:wght@300;400;500;600;700;800;900&display=swap" rel="stylesheet">
<style>
:root{
  --blue:#1f6ff2;
  --blue-dark:#1a4fd6;
  --ink:#0f1522;
  --muted:#5d6675;
  --soft:#f3f5f8;
  --navy:#111a2e;
  --white:#ffffff;
  --red:#d6272a;
  --green:#1c9145;
  --line:#e5e8ee;
  --brand-gray:#b9c1cc;
}
*{box-sizing:border-box;margin:0;padding:0}
html,body{width:1200px;height:3132px;overflow:hidden}
body{font-family:'Lexend',sans-serif;color:var(--ink);background:var(--white);position:relative}
a{color:inherit;text-decoration:none}

.site-header{position:absolute;top:0;left:0;width:1200px;height:77px;background:var(--white);display:flex;align-items:center}
.wordmark{position:absolute;left:67px;display:flex;align-items:center;gap:8px;font-weight:700;font-size:19px;color:var(--blue-dark)}
.wordmark .mark{width:18px;height:18px;background:var(--red);border-radius:3px}
.main-nav{position:absolute;left:386px;display:flex;gap:30px;font-size:13px;color:var(--ink)}
.btn{display:inline-flex;align-items:center;justify-content:center;border-radius:999px;font-weight:700;color:var(--white);background:var(--blue)}
.header-cta{position:absolute;left:963px;top:19px;width:146px;height:37px;font-size:13px;box-shadow:0 4px 10px rgba(31,111,242,.3)}
.cart{position:absolute;left:1126px;top:20px;width:36px;height:36px;border-radius:50%;background:#f1f2f5;display:flex;align-items:center;justify-content:center}

.hero{position:absolute;top:77px;left:0;width:1200px;height:560px;background:radial-gradient(ellipse at 70% 30%,#6a2a2c 0%,#3a2420 35%,#1d2a1f 70%,#142016 100%)}
.hero-photo{position:absolute;inset:0;background:linear-gradient(90deg,rgba(10,14,12,.75) 0%,rgba(10,14,12,.35) 50%,rgba(10,14,12,.1) 100%)}
.hero h1{position:absolute;left:75px;top:150px;font-size:68px;line-height:66px;font-weight:900;color:var(--white);letter-spacing:-.5px}
.hero p{position:absolute;left:75px;top:300px;font-size:18px;line-height:26px;color:var(--white);font-weight:500}
.hero .btn-primary{position:absolute;left:75px;top:389px;width:239px;height:52px;font-size:15px}
.hero .btn-ghost{position:absolute;left:332px;top:389px;width:260px;height:52px;font-size:15px;background:rgba(255,255,255,.14);gap:10px}

.process{position:absolute;top:579px;left:38px;width:1124px;display:flex;gap:16px}
.step{position:relative;width:364px;height:209px;border-radius:32px;padding:30px;color:var(--white);box-shadow:0 14px 26px rgba(0,0,0,.15);overflow:hidden}
.step.blue{background:linear-gradient(135deg,#2f64e8,#1c3cc4)}
.step.red{background:linear-gradient(135deg,#e0312f,#b11a1f)}
.step.green{background:linear-gradient(135deg,#22a24d,#137a35)}
.step .num{position:absolute;right:16px;top:14px;font-size:64px;font-weight:900;color:rgba(255,255,255,.1)}
.step .icon{width:44px;height:44px;border-radius:50%;background:rgba(255,255,255,.22);display:flex;align-items:center;justify-content:center}
.step h3{margin-top:20px;font-size:23px;font-weight:800}
.step p{margin-top:14px;font-size:12.5px;line-height:19px;opacity:.92}

.sports-band{position:absolute;top:637px;left:0;width:1200px;height:584px;background:var(--soft);z-index:-1}
.gear-title{position:absolute;left:38px;top:920px;font-size:44px;font-weight:900}
.view-all{position:absolute;left:1031px;top:936px;font-size:15px;font-weight:600;color:var(--blue)}
.sport-cards{position:absolute;top:1014px;left:38px;display:flex;gap:30px}
.sport-card{width:355px;height:131px;border-radius:32px;padding:30px;font-size:34px;font-weight:800;color:var(--white);box-shadow:0 12px 22px rgba(0,0,0,.16)}
.sport-card.basketball{background:linear-gradient(100deg,#4a3220,#8a6a4a 55%,#a98ab8)}
.sport-card.football{background:linear-gradient(100deg,#1f3f8a,#2c4c9a 45%,#2a2a35)}
.sport-card.baseball{background:linear-gradient(100deg,#2b2522,#6f6560 55%,#5a64b8)}

.champions-title{position:absolute;left:0;width:1200px;top:1290px;text-align:center;font-size:44px;font-weight:900}
.champions-sub{position:absolute;left:0;width:1200px;top:1358px;text-align:center;font-size:17px;color:var(--muted)}
.tile{position:absolute;border-radius:32px;overflow:hidden;box-shadow:0 10px 20px rgba(0,0,0,.14)}
.tile .tag{position:absolute;left:22px;bottom:24px;height:30px;padding:0 16px;border-radius:999px;background:var(--white);font-size:12px;font-weight:700;letter-spacing:1.5px;display:flex;align-items:center}
.tile .tag.accent{background:var(--blue);color:var(--white)}
.t-basketball{left:38px;top:1427px;width:550px;height:551px;background:radial-gradient(circle at 55% 45%,#4a4a44,#1a1a18 75%)}
.t-volleyball{left:612px;top:1427px;width:263px;height:264px;background:linear-gradient(160deg,#3a3a3e,#8b8a90 55%,#2a7f95)}
.t-track{left:898px;top:1427px;width:264px;height:264px;background:linear-gradient(180deg,#3b5a38 0%,#b8563d 45%,#c4603f)}
.t-soccer{left:612px;top:1714px;width:263px;height:264px;background:linear-gradient(180deg,#141c2c 0%,#1c2638 65%,#7a5236)}
.t-hockey{left:898px;top:1714px;width:264px;height:264px;background:linear-gradient(180deg,#9fb0b3,#e4e8e9)}
.t-baseball{left:38px;top:2002px;width:263px;height:263px;background:linear-gradient(180deg,#2c4a30 0%,#3a5c3c 60%,#9c7252)}
.gallery-btn{position:absolute;left:477px;top:2311px;width:248px;height:44px;font-size:13px}

.team-sales{position:absolute;top:2430px;left:0;width:1200px;height:214px;background:var(--navy);color:var(--white)}
.team-sales h2{position:absolute;left:38px;top:60px;font-size:29px;font-weight:800}
.team-sales p{position:absolute;left:38px;top:104px;font-size:17px;line-height:27px;color:#c4cad6;width:520px}
.team-sales .btn{position:absolute;left:953px;top:85px;width:209px;height:45px;font-size:15px}

.footer-brand{position:absolute;left:38px;top:2696px;width:250px}
.footer-brand .wordmark{position:static}
.footer-brand p{margin-top:22px;font-size:12.5px;line-height:19px;color:var(--muted)}
.footer-col{position:absolute;top:2708px}
.footer-col h4{font-size:12px;font-weight:700;letter-spacing:1.8px;margin-bottom:14px}
.footer-col li{list-style:none;font-size:13px;color:var(--muted);margin-bottom:12px}
.socials{display:flex;gap:18px;margin-bottom:18px}
.socials span{width:18px;height:18px;border-radius:4px;background:#d9dde4}
.phone{font-size:13px;color:var(--muted)}
.divider{position:absolute;left:38px;width:1124px;height:1px;background:var(--line)}
.trusted{position:absolute;left:0;width:1200px;top:2944px;text-align:center;font-size:12px;letter-spacing:2px;font-weight:600;color:#9aa3b0}
.brand-row{position:absolute;left:0;width:1200px;top:2984px;display:flex;justify-content:center;gap:60px;font-size:19px;font-weight:800;color:var(--brand-gray);letter-spacing:.5px}
.copyright{position:absolute;left:38px;top:3080px;font-size:12px;color:var(--muted)}
.legal{position:absolute;right:38px;top:3080px;display:flex;gap:22px;font-size:11px;color:#9aa3b0}
</style>
</head>
<body>

<header class="site-header">
  <a class="wordmark" href="#"><span class="mark"></span>Wren Sporting Goods</a>
  <nav class="main-nav">
    <a href="#">Home</a><a href="#">Locker Room</a><a href="#">Custom Uniforms</a><a href="#">Brands</a><a href="#">About</a>
  </nav>
  <a class="btn header-cta" href="#">Start Designing</a>
  <a class="cart" href="#" aria-label="Cart">
    <svg width="14" height="16" viewBox="0 0 14 16"><path d="M4 5V4a3 3 0 0 1 6 0v1" fill="none" stroke="#0f1522" stroke-width="1.6"/><rect x="1" y="5" width="12" height="10" rx="2" fill="#0f1522"/></svg>
  </a>
</header>

<section class="hero">
  <div class="hero-photo" role="img" aria-label="Football players in red jerseys and gold pants walking out onto a stadium field under lights"></div>
  <h1>Design Your Own.<br>Wear Your Pride.</h1>
  <p>Professional-grade custom jerseys &amp; fanwear for<br>Basketball, Football &amp; Baseball.</p>
  <a class="btn btn-primary" href="#">Launch Custom Creator</a>
  <a class="btn btn-ghost" href="#">Explore Team Uniforms
    <svg width="14" height="12" viewBox="0 0 14 12"><path d="M1 6h11M7 1l5 5-5 5" fill="none" stroke="#fff" stroke-width="1.8"/></svg></a>
</section>

<div class="sports-band"></div>

<section class="process">
  <div class="step blue">
    <span class="num">01</span>
    <div class="icon"><svg width="22" height="18" viewBox="0 0 22 18"><path d="M6 16a5 5 0 0 1-.5-10A6.5 6.5 0 0 1 18 7a4.5 4.5 0 0 1-1 9z" fill="#fff"/><path d="M11 14V8M8 10.5l3-3 3 3" fill="none" stroke="#2448d2" stroke-width="1.8"/></svg></div>
    <h3>Upload &amp; Design</h3>
    <p>Upload your team logo, use our templates, or start from scratch with our intuitive builder.</p>
  </div>
  <div class="step red">
    <span class="num">02</span>
    <div class="icon"><svg width="22" height="18" viewBox="0 0 22 18"><path d="M11 5a2 2 0 1 1 2-2M11 5v2L2 14h18l-9-7" fill="none" stroke="#fff" stroke-width="1.8"/></svg></div>
    <h3>Customize Gear</h3>
    <p>Choose from 500+ top-quality jerseys, hoodies, and athletic wear across all major sports.</p>
  </div>
  <div class="step green">
    <span class="num">03</span>
    <div class="icon"><svg width="22" height="16" viewBox="0 0 22 16"><path d="M1 2h12v9H1zM13 5h4l3 3v3h-7z" fill="#fff"/><circle cx="5" cy="13" r="2" fill="#fff"/><circle cx="16" cy="13" r="2" fill="#fff"/></svg></div>
    <h3>Ship &amp; Rep</h3>
    <p>Approve your digital proof with your dedicated rep, and we'll handle the rest, fast.</p>
  </div>
</section>

<h2 class="gear-title">Gear For Your Game</h2>
<a class="view-all" href="#">View all sports →</a>
<section class="sport-cards">
  <a class="sport-card basketball" href="#" role="img" aria-label="Basketball player dribbling a ball">Basketball</a>
  <a class="sport-card football" href="#" role="img" aria-label="Football team in blue jerseys">Football</a>
  <a class="sport-card baseball" href="#" role="img" aria-label="Close-up of a wooden baseball bat">Baseball</a>
</section>

<h2 class="champions-title">Worn By Champions</h2>
<p class="champions-sub">Real teams, real games, real gear. Get inspired by the community.</p>

<div class="tile t-basketball" role="img" aria-label="Basketball player in a white jersey leaping for a dunk"><span class="tag accent">BASKETBALL</span></div>
<div class="tile t-volleyball" role="img" aria-label="Volleyball team celebrating on court"><span class="tag">VOLLEYBALL</span></div>
<div class="tile t-track" role="img" aria-label="Runner tying shoes on a red track"><span class="tag">TRACK &amp; FIELD</span></div>
<div class="tile t-soccer" role="img" aria-label="Soccer player in a green shirt with a ball"><span class="tag">SOCCER</span></div>
<div class="tile t-hockey" role="img" aria-label="Hockey player skating with a stick"><span class="tag">HOCKEY</span></div>
<div class="tile t-baseball" role="img" aria-label="Baseball pitcher in a blue jersey mid-throw"><span class="tag">BASEBALL</span></div>

<a class="btn gallery-btn" href="#">View Gallery &amp; Get Inspired</a>

<section class="team-sales">
  <h2>Ordering for a Team or League?</h2>
  <p>Get a dedicated rep, bulk pricing discounts, and free vector design help from our pros.</p>
  <a class="btn" href="#">Contact Team Sales</a>
</section>

<div class="footer-brand">
  <a class="wordmark" href="#"><span class="mark"></span>Wren Sporting Goods</a>
  <p>Empowering teams to look as good as they play. Quality custom apparel for every sport.</p>
</div>
<div class="footer-col" style="left:328px">
  <h4>SHOP</h4>
  <ul><li>Jerseys</li><li>Fanwear</li><li>Accessories</li><li>Team Packs</li></ul>
</div>
<div class="footer-col" style="left:619px">
  <h4>SUPPORT</h4>
  <ul><li>Order Status</li><li>Sizing Charts</li><li>Contact Us</li><li>Returns</li></ul>
</div>
<div class="footer-col" style="left:909px">
  <h4>STAY CONNECTED</h4>
  <div class="socials"><span></span><span></span><span></span></div>
  <div class="phone">1-800-555-0147</div>
</div>

<div class="divider" style="top:2906px"></div>
<div class="trusted">TRUSTED BRANDS WE USE</div>
<div class="brand-row"><span>VANTOR</span><span>HALDEN</span><span>IRON CREST</span><span>SUMMITRA</span><span>PAXEL</span></div>
<div class="divider" style="top:3048px"></div>
<div class="copyright">© 2025 Wren Sporting Goods. All rights reserved.</div>
<div class="legal"><span>Privacy Policy</span><span>Terms of Service</span></div>

</body>
</html>
```